company profile catalogue for Architecture and Interior Design and project management company

We target private customers who want to design a villa or a residential palace. We also target international brands, restaurants, furniture stores and malls.

Our logo on the front page.
Simple but inviting and professional.
The goal is to convey to the customer that we are professional design professionals and professional contractors.
And accuracy in action.
And commitment to the duration of the project.

We are Architectural and Interior design firm and we want a company profile catalogue which has the following:

Three sections with a small difference in theme (in colors) which demo the following
(It contains a group of projects with photos with a description for each photo included) :
A- (Architectural design)
B- (Interior design)
C- (Contracting and Project management)

We want only (7) pages to be designed, which will contain the following:
1- Front Cover page
2- Back cover page
3- Introduction page (Text & 1 Picture)
4- Document page (contain also text w/o 1 picture)
5&6&7- Three pages (which will contain pictures for project and should be flexible, their scheme as following:)
• Contain 1 picture with text
• Contain 2 pictures with text
• Contain 3 pictures with text

Notes:
1- The catalog structure guide also included
2- We have attached our current profile so you can take an idea how the main structure of the catalog (87MB):
https://www.filecrate-example.net/s/qmra82pzk4lwtcn/k%26mprofile2017-rev1.1.pdf?dl=0
3- We also attached the logo of our firm

Target Market(s)

Industry/Entity Type

Architecture

Font styles to use
Serif

Requirements
Must have
• Our logo on the front page.
• Simple but inviting and professional.
• The goal is to convey to the customer that we are professional design professionals and professional contractors.
• And accuracy in action.
• And commitment to the duration of the project.
Nice to have
• Our logo and The distinctive colors of each department
Should not have
• Should not use anything from the previous design, we are looking for something new and elegant.

```html
<!DOCTYPE html>
<html lang="en">
<head>
<meta charset="utf-8">
<title>Company Profile – Document Page Spread</title>
<link rel="stylesheet" href="https://fonts.googleapis.com/css2?family=Montserrat:wght@500;600&family=Didact+Gothic&display=swap">
<style>
  :root {
    --backdrop: #8c8c8c;
    --paper: #ffffff;
    --photo-tone-a: #b9b5aa;
    --photo-tone-b: #8f8a7f;
    --brand-blue: #1f5fa8;
    --tab-grey: #8a8a8a;
    --body-ink: #3a3a3a;
    --caption-ink: #111111;
  }
  * { margin: 0; padding: 0; box-sizing: border-box; }
  html, body { width: 1200px; height: 1000px; overflow: hidden; }
  body { background: var(--backdrop); position: relative; font-family: "Didact Gothic", sans-serif; }

  .spread { position: absolute; left: 40px; top: 285px; width: 1130px; height: 405px; display: flex; }
  .page { position: relative; height: 100%; }
  .page--left { width: 560px; }
  .page--right { width: 570px; background: var(--paper); }

  .feature-photo {
    position: absolute; inset: 0;
    background: radial-gradient(ellipse at 60% 25%, #d2cec4 0%, var(--photo-tone-a) 40%, var(--photo-tone-b) 100%);
  }

  .page-footer { position: absolute; bottom: 28px; font-size: 6px; letter-spacing: 0.2px; }
  .page--left .page-footer { right: 76px; color: #ffffff; }
  .page--right .page-footer { left: 72px; color: #555555; }

  .section-tab { position: absolute; display: flex; align-items: center; justify-content: center;
    font-family: "Montserrat", sans-serif; font-weight: 600; font-size: 18px; color: #ffffff; white-space: nowrap; }
  .section-tab--current { left: 525px; top: 362px; width: 75px; height: 253px; background: var(--brand-blue); }
  .section-tab--current span { transform: rotate(-90deg); }
  .section-tab--next { left: 600px; top: 362px; width: 70px; height: 253px; }
  .section-tab--next svg { position: absolute; inset: 0; }
  .section-tab--next span { position: relative; transform: rotate(90deg); }

  .brand { position: absolute; right: 40px; top: 30px; display: flex; align-items: center; gap: 4px;
    font-size: 8px; color: var(--brand-blue); }
  .brand-square { width: 8px; height: 8px; background: var(--brand-blue); }

  .body-copy { position: absolute; left: 140px; top: 66px; width: 335px; }
  .body-copy p { font-size: 7.4px; line-height: 8px; color: var(--body-ink); text-align: justify; margin-bottom: 8px; }
  .body-copy p:nth-child(5) { margin-top: 14px; }

  .spread-caption { position: absolute; left: 0; width: 1170px; top: 710px; text-align: center;
    font-family: "Montserrat", sans-serif; font-weight: 500; font-size: 22px; color: var(--caption-ink); letter-spacing: 0.3px; }
</style>
</head>
<body>
  <div class="spread">
    <section class="page page--left">
      <div class="feature-photo" role="img" aria-label="Photograph of a grand palace lobby interior with chandelier, arched balconies and lounge seating, softened with a grey overlay"></div>
      <div class="page-footer">Document &nbsp;|&nbsp; Page #1</div>
    </section>
    <section class="page page--right">
      <div class="brand"><span class="brand-square"></span>Meridian Atelier</div>
      <div class="body-copy">
        <p>Lorem ipsum dolor sit amet, consectetur adipiscing elit, sed do eiusmod tempor incididunt ut labore et dolore magna aliqua. Ut enim ad minim veniam, quis nostrud exercitation ullamco laboris nisi ut aliquip ex ea commodo consequat. Duis aute irure dolor in reprehenderit in voluptate velit esse cillum dolore eu fugiat nulla pariatur. Excepteur sint occaecat cupidatat non proident, sunt in culpa qui officia deserunt mollit anim id est laborum.</p>
        <p>Lorem ipsum dolor sit amet, consectetur adipiscing elit, sed do eiusmod tempor incididunt ut labore et dolore magna aliqua. Ut enim ad minim veniam, quis nostrud exercitation ullamco laboris nisi ut aliquip ex ea commodo consequat. Duis aute irure dolor in reprehenderit in voluptate velit esse cillum dolore eu fugiat nulla pariatur. Excepteur sint occaecat cupidatat non proident, sunt in culpa qui officia deserunt mollit anim id est laborum.</p>
        <p>Lorem ipsum dolor sit amet, consectetur adipiscing elit, sed do eiusmod tempor incididunt ut labore et dolore magna aliqua. Ut enim ad minim veniam, quis nostrud exercitation ullamco laboris nisi ut aliquip ex ea commodo consequat. Duis aute irure dolor in reprehenderit in voluptate velit esse cillum dolore eu fugiat nulla pariatur. Excepteur sint occaecat cupidatat non proident, sunt in culpa qui officia deserunt mollit anim id est laborum.</p>
        <p>Lorem ipsum dolor sit amet, consectetur adipiscing elit, sed do eiusmod tempor incididunt ut labore et dolore magna aliqua. Ut enim ad minim veniam, quis nostrud exercitation ullamco laboris nisi ut aliquip ex ea commodo consequat. Duis aute irure dolor in reprehenderit in voluptate velit esse cillum dolore eu fugiat nulla pariatur. Excepteur sint occaecat cupidatat non proident, sunt in culpa qui officia deserunt mollit anim id est laborum.</p>
        <p>Lorem ipsum dolor sit amet, consectetur adipiscing elit, sed do eiusmod tempor incididunt ut labore et dolore magna aliqua. Ut enim ad minim veniam, quis nostrud exercitation ullamco laboris nisi ut aliquip ex ea commodo consequat. Duis aute irure dolor in reprehenderit in voluptate velit esse cillum dolore eu fugiat nulla pariatur. Excepteur sint occaecat cupidatat non proident, sunt in culpa qui officia deserunt mollit anim id est laborum.</p>
      </div>
      <div class="page-footer">Page #2 &nbsp;|&nbsp; Document</div>
    </section>
  </div>

  <div class="section-tab section-tab--current"><span>Document Page #1</span></div>
  <div class="section-tab section-tab--next">
    <svg width="70" height="253" viewBox="0 0 70 253" aria-hidden="true">
      <polygon points="0,0 70,10 70,241 0,253" fill="var(--tab-grey)"/>
    </svg>
    <span>Document Page #2</span>
  </div>

  <div class="spread-caption">DOCUMENT PAGE</div>
</body>
</html>
```